Bottle Label for New Brand of Boody Mary mix

We need a logo and label design for a new brand of bloody mary mix, the mix has Vodka premixed with all the spices and tomato juice, and all you add is the ice!
Currently under ingredient breakdown and government approval, looking to role out in a few months. Ideas for names are as follows, 'OAK RUN' or "MOSS HARBOR" or 'Plumbrook' (like the bird, maybe Gold Plumbrook) very open to all ideas, important to help consumer to remember the brand and understand is has everything included, all you need is ICE!

I have the owners of the mix reviewing the designs, will have feed back soon.

Thank you

```html
<!DOCTYPE html>
<html lang="en">
<head>
<meta charset="utf-8">
<title>Ember Row – Tomato and Vodka Blend Label</title>
<link rel="stylesheet" href="https://fonts.googleapis.com/css2?family=Cinzel:wght@600&family=Cormorant+Garamond:wght@600;700&display=swap">
<style>
  :root {
    --label-red: #a80000;
    --label-white: #ffffff;
  }
  html, body {
    margin: 0;
    padding: 0;
    width: 1200px;
    height: 1000px;
    overflow: hidden;
    background: var(--label-white);
  }
  .label {
    position: relative;
    width: 1200px;
    height: 1000px;
    overflow: hidden;
    background: var(--label-white);
  }
  .label__art {
    position: absolute;
    inset: 0;
    display: block;
  }
  .brand-name {
    font-family: "Cormorant Garamond", Georgia, serif;
    font-weight: 700;
    font-size: 150px;
    letter-spacing: 4px;
    fill: var(--label-red);
  }
  .brand-tagline {
    font-family: "Cormorant Garamond", Georgia, serif;
    font-weight: 600;
    font-size: 46px;
    letter-spacing: 12px;
    fill: var(--label-red);
  }
  .emblem-name {
    font-family: "Cormorant Garamond", Georgia, serif;
    font-weight: 700;
    font-size: 132px;
    fill: var(--label-red);
  }
  .call-to-action {
    font-family: "Cinzel", "Times New Roman", serif;
    font-weight: 600;
    font-size: 62px;
    fill: var(--label-white);
  }
  .cta-dot { fill: var(--label-white); }
  .stripe-red { fill: var(--label-red); }
  .stripe-white { fill: var(--label-white); }
</style>
</head>
<body>
<main class="label">
  <svg class="label__art" width="1200" height="1000" viewBox="0 0 1200 1000" xmlns="http://www.w3.org/2000/svg">
    <g class="header-band">
      <rect class="stripe-red" x="0" y="0" width="1200" height="322"/>
      <rect class="stripe-white" x="0" y="22" width="1200" height="20"/>
      <rect class="stripe-white" x="0" y="88" width="1200" height="20"/>
      <rect class="stripe-white" x="0" y="155" width="1200" height="20"/>
      <rect class="stripe-white" x="0" y="222" width="1200" height="20"/>
    </g>

    <g class="body-stripes">
      <rect class="stripe-red" x="0" y="412" width="1200" height="66"/>
      <rect class="stripe-red" x="0" y="565" width="1200" height="67"/>
      <rect class="stripe-red" x="0" y="722" width="1200" height="66"/>
    </g>

    <g class="name-plate">
      <rect class="stripe-white" x="168" y="18" width="896" height="274"/>
      <rect class="stripe-red" x="178" y="28" width="876" height="254"/>
      <rect class="stripe-white" x="206" y="54" width="822" height="200"/>
      <text class="brand-name" x="620" y="168" text-anchor="middle">Ember Row</text>
      <text class="brand-tagline" x="618" y="230" text-anchor="middle">Tomato and Vodka Blend</text>
    </g>

    <g class="emblem">
      <circle class="stripe-white" cx="600" cy="600" r="292"/>
      <circle class="stripe-red" cx="600" cy="600" r="280"/>
      <circle class="stripe-white" cx="600" cy="600" r="266"/>
      <circle class="stripe-red" cx="600" cy="600" r="260"/>
      <circle class="stripe-white" cx="600" cy="600" r="252"/>
      <text class="emblem-name" x="600" y="585" text-anchor="middle">Ember</text>
      <text class="emblem-name" x="600" y="705" text-anchor="middle">Row</text>
    </g>

    <g class="footer-band">
      <rect class="stripe-red" x="0" y="885" width="1200" height="115"/>
      <g class="cta-dots cta-dots--left">
        <circle class="cta-dot" cx="196" cy="950" r="8"/>
        <circle class="cta-dot" cx="224" cy="950" r="8"/>
        <circle class="cta-dot" cx="252" cy="950" r="8"/>
        <circle class="cta-dot" cx="280" cy="950" r="8"/>
        <circle class="cta-dot" cx="308" cy="950" r="8"/>
      </g>
      <text class="call-to-action" x="613" y="973" text-anchor="middle">JUST ADD ICE !</text>
      <g class="cta-dots cta-dots--right">
        <circle class="cta-dot" cx="916" cy="950" r="8"/>
        <circle class="cta-dot" cx="944" cy="950" r="8"/>
        <circle class="cta-dot" cx="972" cy="950" r="8"/>
        <circle class="cta-dot" cx="1000" cy="950" r="8"/>
        <circle class="cta-dot" cx="1028" cy="950" r="8"/>
      </g>
    </g>
  </svg>
</main>
</body>
</html>
```